Redesign of Medical App for Patients

• The Designer’s task is to provide a new fully-responsive design for our apps, and then code it using only basic html and CSS.
• Your design will be incorporated into our existing REACT native app.

Target Market(s)

Medical Patients

Industry/Entity Type

Medical

Coding

Coded - Design and coding required

Number of Pages Required

5+ page

Requirements
Must have
• Short list candidates will receive detailed briefing
Nice to have
• detailed briefing contains some of our ideas.

```html
<!DOCTYPE html>
<html lang="en">
<head>
<meta charset="utf-8">
<title>MediPath – App Screens</title>
<link href="https://fonts.googleapis.com/css2?family=Open+Sans:wght@400;600;700&display=swap" rel="stylesheet">
<style>
:root{
  --canvas:#ffffff;
  --navy:#165a7e;
  --accent:#1f7fb6;
  --ink:#2b2b2b;
  --muted:#5d6369;
  --card:#ffffff;
  --shadow:rgba(0,0,0,.16);
}
*{box-sizing:border-box;margin:0;padding:0}
html,body{width:1200px;height:656px;overflow:hidden;background:var(--canvas)}
body{font-family:"Open Sans",sans-serif;color:var(--ink);position:relative}
.screen{position:absolute;top:45px;width:163px;background:var(--card);box-shadow:0 0 3px var(--shadow);overflow:hidden}
.screen--splash{left:39px;height:289px}
.screen--board{left:224px;height:289px}
.screen--foot{left:409px;height:472px}
.screen--bariatric{left:595px;height:370px}
.screen--fertility{left:780px;height:510px}
.screen--shoulder{left:966px;height:289px}

.brand{position:absolute;left:16px;top:133px;display:flex;align-items:center;gap:4px}
.brand__dot{width:24px;height:24px;border-radius:50%;background:var(--accent);flex:none}
.brand__name{font-size:17px;font-weight:600;color:var(--ink);letter-spacing:-.2px}

.band{position:relative;background:var(--navy);height:88px}
.band--short{height:48px}
.back{position:absolute;left:8px;top:7px;width:8px;height:8px}
.title{position:absolute;left:0;right:0;top:5px;text-align:center;color:#fff;font-size:6.2px;font-weight:700}
.band__art{position:absolute;left:16px;top:29px;width:54px;height:50px;border-radius:3px}
.art--foot{background:linear-gradient(135deg,#1d4fa8 0%,#2f74d0 45%,#f07a1a 60%,#1a3f8c 100%)}
.art--stomach{background:radial-gradient(circle at 55% 55%,#e0806e 0%,#b23a2c 45%,#6b1410 100%)}
.art--fertility{background:linear-gradient(135deg,#c2412e 0%,#8a2a22 45%,#b98a86 75%,#6c4a4a 100%)}
.art--shoulder{background:linear-gradient(135deg,#1b3f9c 0%,#3a7ad8 45%,#e5572a 62%,#1a3a8a 100%)}
.menu{position:absolute;left:75px;top:33px;list-style:none;color:#fff;font-size:4.3px}
.menu li{height:10.7px;display:flex;align-items:flex-start;gap:3px}
.menu li::before{content:"";width:2.4px;height:2.4px;border-radius:50%;background:#fff;margin-top:1px}

.content{padding:12px 8px 0 16px}
.section+.section{margin-top:10px}
.section h3{font-size:5.1px;font-weight:700;color:var(--accent);line-height:8px;margin-bottom:2px}
.section p{font-size:4.3px;line-height:7.85px;color:var(--muted)}

.advisors{position:absolute;left:8px;top:32px;width:146px}
.advisor{height:43px;background:var(--card);border-radius:2px;box-shadow:0 0 3px var(--shadow);position:relative;margin-bottom:8px}
.advisor__photo{position:absolute;left:8px;top:6px;width:27px;height:31px;background:linear-gradient(180deg,#c9b7a6,#8b6f5d)}
.advisor__name{position:absolute;left:46px;top:7px;font-size:5.1px;font-weight:700;color:var(--ink)}
.advisor__role{position:absolute;left:46px;top:16px;right:8px;font-size:4.2px;line-height:6.2px;color:var(--muted)}
</style>
</head>
<body>

<section class="screen screen--splash">
  <div class="brand"><span class="brand__dot"></span><span class="brand__name">MEDIPATH</span></div>
</section>

<section class="screen screen--board">
  <header class="band band--short">
    <svg class="back" viewBox="0 0 8 8"><rect x=".4" y=".4" width="7.2" height="7.2" rx="1" fill="none" stroke="#fff" stroke-width=".7"/><path d="M5.8 4H2.2M3.6 2.6 2.2 4l1.4 1.4" fill="none" stroke="#fff" stroke-width=".7"/></svg>
    <h1 class="title">Medical Advisory Board</h1>
  </header>
  <div class="advisors">
    <article class="advisor"><div class="advisor__photo" role="img" aria-label="Portrait photo of advisor"></div><h2 class="advisor__name">Helena M. Varga, MD</h2><p class="advisor__role">Professor of Orthopaedic Surgery, Northfield Medical School.</p></article>
    <article class="advisor"><div class="advisor__photo" role="img" aria-label="Portrait photo of advisor"></div><h2 class="advisor__name">Martin C. Osgood, MD MS FNBS</h2><p class="advisor__role">Professor of Surgery, Northfield Medical School.</p></article>
    <article class="advisor"><div class="advisor__photo" role="img" aria-label="Portrait photo of advisor"></div><h2 class="advisor__name">Victor L. Brannan, MD MBA</h2><p class="advisor__role">Associate Professor of Orthopaedic Surgery, Northfield Medical School.</p></article>
    <article class="advisor"><div class="advisor__photo" role="img" aria-label="Portrait photo of advisor"></div><h2 class="advisor__name">Gregory T. Halden, MD MBA</h2><p class="advisor__role">Assistant Professor of Obstetrics, Gynecology and Reproductive Biology, Northfield Medical School. Vice President, Northfield Faculty Physicians.</p></article>
  </div>
</section>

<section class="screen screen--foot">
  <header class="band">
    <svg class="back" viewBox="0 0 8 8"><rect x=".4" y=".4" width="7.2" height="7.2" rx="1" fill="none" stroke="#fff" stroke-width=".7"/><path d="M5.8 4H2.2M3.6 2.6 2.2 4l1.4 1.4" fill="none" stroke="#fff" stroke-width=".7"/></svg>
    <h1 class="title">Orthopaedics - Foot &amp; Ankle</h1>
    <div class="band__art art--foot" role="img" aria-label="Illustration of a foot and ankle skeleton with highlighted joint"></div>
    <ul class="menu"><li>Series Editor</li><li>Authors</li><li>Procedures</li></ul>
  </header>
  <div class="content">
    <div class="section"><h3>Series Editor:</h3><p>Victor L. Brannan MD MBA<br>Associate Professor of Orthopaedic Surgery<br>Northfield Medical School</p></div>
    <div class="section"><h3>Authors:</h3><p>Owen R. Castell MD<br>Instructor of Orthopaedic Surgery, Northfield Medical School<br>Lucas D. Fenwick MD<br>Assistant Professor of Orthopedic Surgery, Northfield Medical<br>School</p></div>
    <div class="section"><h3>Authors:</h3><p>Lumbar disc hernia/microdiskectomy<br>Ankle fracture<br>Achilles Rupture<br>Ankle replacement<br>Ankle fusion<br>Midfoot fusion<br>First Metatarsophalangeal (MTP) Joint Fusion<br>First Metatarsophalangeal (MTP) Joint Cheilectomy<br>Ankle arthroscopy<br>Ankle Instability<br>Flat foot reconstruction<br>Hind foot fusion<br>Bunion Correction – Open<br>Hammertoe Correction – Open<br>Haglunds – Open<br>First Metatarsophalangeal Joint Fusion – Open<br>Bunion Correction - MIS<br>Hammertoe Correction - MIS<br>Haglunds - MIS<br>First Metatarsophalangeal Joint Fusion - MIS<br>Ankle Brostrom - MIS<br>Zadek Osteotomy - MIS<br>Lisfranc Injury<br>Peroneal Tendon repair<br>Calcaneal Fracture<br>Talus Fracture<br>Metatarsal Fracture<br>Tarsal Tunnel release<br>Plantar Fasciotomy<br>Toe Fracture<br>Gastrocnemius Recession</p></div>
  </div>
</section>

<section class="screen screen--bariatric">
  <header class="band">
    <svg class="back" viewBox="0 0 8 8"><rect x=".4" y=".4" width="7.2" height="7.2" rx="1" fill="none" stroke="#fff" stroke-width=".7"/><path d="M5.8 4H2.2M3.6 2.6 2.2 4l1.4 1.4" fill="none" stroke="#fff" stroke-width=".7"/></svg>
    <h1 class="title">Bariatric Surgery</h1>
    <div class="band__art art--stomach" role="img" aria-label="Illustration of a human stomach"></div>
    <ul class="menu"><li>Series Editor</li><li>Authors</li><li>Reviewers</li><li>Procedures</li></ul>
  </header>
  <div class="content">
    <div class="section"><h3>Series Editor:</h3><p>Martin C. Osgood, MD MS FNCS<br>Professor of Surgery<br>Northfield Medical School</p></div>
    <div class="section"><h3>Authors:</h3><p>Adrian K. Mercer MD MPH<br>Samir H. Khalil-Nour MD MBBS<br>Elliot Brand MD<br>Martin C. Osgood, MD MS FNCS</p></div>
    <div class="section"><h3>Reviewers:</h3><p>Nadia Perrin MD<br>Kevin Tran MD<br>Paul R. Sequeira MD FNCS<br>Karim Yasin Haddad MD FNCS<br>Rami J. Saleh MD<br>Quinn E. Hartley MD<br>Walter F. Lindqvist MD</p></div>
    <div class="section"><h3>Procedures:</h3><p>Laparoscopic Cholecystectomy<br>Robotic Cholecystectomy<br>Laparoscopic sleeve gastrectomy<br>Laparoscopic Roux-en Y Gastric bypass<br>Laparoscopic Gastric Band<br>Laparoscopic Adjustable Gastric Band<br>Laparoscopic Colectomy<br>Intragastric balloon<br>Endoscopic Gastric sleeve<br>Robotic Colectomy w ERAS (NCRS version)</p></div>
  </div>
</section>

<section class="screen screen--fertility">
  <header class="band">
    <svg class="back" viewBox="0 0 8 8"><rect x=".4" y=".4" width="7.2" height="7.2" rx="1" fill="none" stroke="#fff" stroke-width=".7"/><path d="M5.8 4H2.2M3.6 2.6 2.2 4l1.4 1.4" fill="none" stroke="#fff" stroke-width=".7"/></svg>
    <h1 class="title">Fertility Medicine</h1>
    <div class="band__art art--fertility" role="img" aria-label="Illustration of an egg cell and sperm"></div>
    <ul class="menu"><li>Series Editor</li><li>Authors</li><li>Procedures</li></ul>
  </header>
  <div class="content">
    <div class="section"><h3>Series Editor:</h3><p>Ethan J. Carrow MD<br>Associate Professor of Obstetrics, Gynecology and Reproductive<br>Biology<br>Northfield Medical School</p></div>
    <div class="section"><h3>Authors:</h3><p>Ethan J. Carrow MD<br>Marco V. Bellini MD<br>Fiona Reyes MD<br>Grace Ann Whitlow MD<br>Samuel Okoro MD<br>Diego M. Santoro MD<br>Sophia Kallis MD<br>Claire Van Hoek L.Ac.<br>Nolan P. Reid MD<br>Julia Marsh MD</p></div>
    <div class="section"><h3>Procedures:</h3><p>IVF - 4 sections<br>Embryo Transfer<br>IUI - Sperm placement<br>Egg Retrieval<br>Egg Freezing - 3 sections<br>Laparoscopic &amp; Robot-Assisted Laparoscopic Myomectomy<br>Ovulation Induction (OI) w. time Intercourse and IUI<br>Unmedicated treatment cycles: Intrauterine insemination<br>Donor Egg IVF - Options &amp; Testing<br>Fertility Assessment/Evaluation<br>Peak Fertility/Ovulation Predictor<br>Pregnancy Loss<br>Early Pregnancy Assessment EPAS OB<br>Uterine Cavity/Fallopian Tube Evaluation Suite<br>Acupuncture Treatments<br>Hysteroscopic polypectomy<br>Hysteroscopic myomectomy<br>Abdominal, Open Laparotomy Myomectomy<br>Hysteroscopic division/resection of uterine septum (aka<br>hysteroscopic septoplasty)<br>Hysteroscopic resection of chronic retained products of<br>conception<br>Hysteroscopic treatment of uterine isthmocele<br>Surgical Sperm Retrieval<br>Microsurgical Varicocelectomy<br>Vasectomy reversal<br>Lifestyle Optimization<br>Fertility Medication Injections<br>Penile Implant<br>LGBTQ+ Family Building</p></div>
  </div>
</section>

<section class="screen screen--shoulder">
  <header class="band">
    <svg class="back" viewBox="0 0 8 8"><rect x=".4" y=".4" width="7.2" height="7.2" rx="1" fill="none" stroke="#fff" stroke-width=".7"/><path d="M5.8 4H2.2M3.6 2.6 2.2 4l1.4 1.4" fill="none" stroke="#fff" stroke-width=".7"/></svg>
    <h1 class="title">Orthopaedics – Sports &amp; Shoulder</h1>
    <div class="band__art art--shoulder" role="img" aria-label="Illustration of a shoulder skeleton with highlighted joint"></div>
    <ul class="menu"><li>Series Editor</li><li>Authors</li><li>Procedures</li></ul>
  </header>
  <div class="content">
    <div class="section"><h3>Series Editor:</h3><p>Victor L. Brannan MD MBA<br>Associate Professor of Orthopaedic Surgery<br>Northfield Medical School</p></div>
    <div class="section"><h3>Authors:</h3><p>Victor L. Brannan MD MBA</p></div>
    <div class="section"><h3>Procedures:</h3><p>Reverse Total Shoulder<br>Total Shoulder Replacement<br>Shoulder Hemiarthroplasty<br>ORIF Proximal Humerus Fracture<br>Open AC/CC ligament reconstruction<br>Open Distal Clavicle Excision<br>Open Shoulder Stabilization (Bankart Procedure)<br>Open Coracoid Transfer (Laterjet Procedure)<br>Arthroscopic Rotator Cuff Repair (Small, Medium, and Large)<br>Arthroscopic Shoulder Stabilization<br>Arthroscopic Shoulder Debridement<br>Open Biceps Tenodesis</p></div>
  </div>
</section>

</body>
</html>
```